Web re-design project for web software development agency

We need to re-design our existing website (www.tovenmedia.co.uk), and are going to start using a shorter domain (www.toven.com).
We have been in business for 8 years and it's time for an update.

We are based at Harrowmede Court (home of the code breakers). We specialise in writing software for the web. Over the years we have built up a healthy customer base and it is time to incorporate the features we build for our customers into our own site (e.g. social media).

We have a team of 8 talented developers with varied skills including: apps for mobile; complex server side software; front-end software; eCommerce software; specialised web based applications; integration software; hardware support; consultancy services. Our customers are diverse (e.g. banking; commerce; veterinary; R&D; health sector; law; accounting; film industry etc.).

Our current colour scheme is blue, white and green although we are not averse to moving away from these colours. We will also be dropping the DESIGN from our name and logo. Revised logo will be attached.

The site needs to be modern, sophisticated and leading edge. We want to show visitors to the site that we are a professional organisation.
Updates

Our logo in PSD format has been uploaded. Please drop the word DESIGN from the logo.

The deliverable for this project is a PSD (ideally we would like to see how the home page, portfolio page, resources page with mugshots, and forms are going to look).

Many thanks,
Tom

Please DO NOT include a Careers section 

We will also need a "meet our team" section with spaces for 10 photographs as well as some space underneath them so that we can add a short paragraph for each one of them.

Target Market(s)

Mainly large corporations needing bespoke web software, or generally complex projects (for anyone).

Industry/Entity Type

Software

Requirements
Must have
• We would like a home page designed that has the following elements on it:
- Show the new cookie compliance policy displayed probably in the top of the page (will disappear).
- A client Testimonial.
- Pricing icon.
- Social media Links.
- A Quote section in expand/collapse field as in (http://www.quillbrook-online.co.uk/our-services.shtml)

We would also like a portfolio page that showcases our clients in an interesting way.

Finally, we would like a form design that we can use throughout the site (i.e. how should buttons, radio buttons, checkboxes, dropdowns, text areas etc. look)?
Nice to have
• A page that follows these guidelines:
http://www.pagerivet.com/the-anatomy-of-a-perfect-landing-page

Here are a few examples of sites in our sector that we like:
- http://www.tidewell-studio.com/
- http://plinthos.co.uk/
- http://www.fernaxis.com/services/web-development (nice contact us page)
- http://www.quillbrook-online.co.uk/
- http://www.lumsa.com/
- http://www.netmoxa.co.uk/
Should not have
• No flash elemets. If anything, we will use html5.

```html
<!DOCTYPE html>
<html lang="en">
<head>
<meta charset="utf-8">
<title>Toven – Home</title>
<link href="https://fonts.googleapis.com/css2?family=Signika:wght@400;600&family=Open+Sans:wght@400;600;700&family=Noto+Serif:ital@1&display=swap" rel="stylesheet">
<style>
:root{
  --sea:#1fa9b3; --sea-deep:#128f9c;
  --navy:#0f4d74; --lime:#c8d42a;
  --ink:#2d5f7a; --text:#1d5d86; --olive:#5a4a10; --brown:#6b4a12;
  --panel:#ffffff; --line:#e3e8ea;
  --modal-frame:#8bbcc8; --modal-bg:#ececec; --field:#e4e3e3; --label:#dcdcdc;
  --clients-bar:#d6e8ee; --footer-band:#f1f0ea; --login:#e8541c;
}
*{box-sizing:border-box;margin:0;padding:0}
html,body{width:1200px;height:955px;overflow:hidden}
body{position:relative;font-family:"Signika",sans-serif;background:linear-gradient(180deg,#21adb8 0%,#1aa3ae 50%,#25b1ba 100%)}
.abs{position:absolute}

.cookie-tab{left:757px;top:0;width:294px;height:30px;background:linear-gradient(#fff,#eef3f3);border-radius:0 0 6px 6px;text-align:center;font-size:12px;line-height:30px;color:#8a9a9e;letter-spacing:.5px}

.brand{left:87px;top:20px;display:flex;align-items:flex-end;gap:10px;height:72px}
.brand-mark{width:36px;height:36px;background:var(--lime);margin-bottom:36px}
.brand-name{font-size:40px;font-weight:600;color:var(--navy);letter-spacing:1px;line-height:1}

.main-nav{left:610px;top:50px;width:447px;height:38px;background:linear-gradient(#fff,#eef3f4);border-radius:4px;display:flex;align-items:center;justify-content:space-around;font-size:12px;color:var(--ink);letter-spacing:.6px;box-shadow:0 2px 4px rgba(0,0,0,.15)}
.main-nav span+span{border-left:1px solid #d8e0e2;padding-left:24px}

.page{left:81px;top:108px;width:982px;height:830px;background:var(--panel);border-radius:10px}

.hero{left:97px;top:117px;width:951px;height:238px;border-radius:8px;background:radial-gradient(circle at 20% 20%,#6d4f9e,#2a1d55 55%,#101830)}
.hero-art{left:130px;top:170px;width:220px;height:135px;background:linear-gradient(135deg,#6ab8e6,#1b4fa8);border:3px solid #fff}
.hero-title{left:496px;top:148px;color:#fff;font-size:17px;letter-spacing:.6px}

.section-title{font-size:15px;color:var(--ink)}
.service-card{left:104px;top:403px;width:236px;height:177px;border-top:1px solid var(--line)}
.service-icon{left:170px;top:420px;width:90px;height:90px;background:radial-gradient(#c7d3da,#fff 70%)}
.service-text{left:108px;top:528px;width:228px;font-size:11px;line-height:21px;color:var(--text);text-align:center}
.service-card-2{left:341px;top:403px;width:22px;height:177px;border-left:1px solid var(--line);font-size:11px;color:var(--text);padding:124px 0 0 14px;line-height:21px}
.btn-grey{background:linear-gradient(#fafafa,#e4e4e4);border:1px solid #cfcfcf;border-radius:3px;font-size:12px;color:#555;display:flex;align-items:center;justify-content:center}

.news-date{font-size:11px;font-weight:600;color:var(--brown)}
.news-text{font-size:11px;color:#5a5a4a;line-height:15px}
.link-accent{font-size:11px;color:#2b8fb4}
.num-accent{font-size:11px;color:#b59a1c}

.clients-bar{left:88px;top:622px;width:967px;height:40px;border-radius:8px;background:linear-gradient(#e6f2f5,var(--clients-bar));font-size:15px;color:#444;padding:12px 0 0 21px}
.client-box{left:105px;top:663px;width:275px;height:132px;background:#efeded;border:1px solid #dcdcdc}
.client-name{left:158px;top:669px;width:159px;height:114px;background:#e8f3f8;display:flex;align-items:center;justify-content:center;font-size:22px;color:#2a86c6}
.circle-btn{width:20px;height:20px;border-radius:50%;background:linear-gradient(#fff,#ccc);border:1px solid #999}

.testimonial{left:765px;top:694px;width:285px;font-size:11px;color:#555;line-height:14.5px}
.testimonial-author{left:887px;top:805px;font-size:13px;color:#555}
.avatar{left:995px;top:766px;width:52px;height:52px;background:linear-gradient(#8a7a76,#4a3d3a);border-radius:4px}

.footer-band{left:81px;top:845px;width:982px;height:44px;background:var(--footer-band);border-top:1px solid #e0ddd0;border-bottom:1px solid #e0ddd0}
.share-strip{left:155px;top:858px;width:308px;height:26px;background:#fff;border-radius:4px;display:flex;gap:6px;align-items:center;padding:0 6px}
.share-btn{height:18px;border:1px solid #c9c9c9;border-radius:3px;background:#f5f5f5;font-size:11px;color:#333;padding:0 6px;line-height:16px}
.share-count{height:18px;border:1px solid #ccc;font-size:10px;padding:0 4px;line-height:16px;color:#555}
.follow-label{left:824px;top:858px;font-size:14px;color:var(--olive)}
.follow-icons{left:914px;top:853px;display:flex;gap:6px}
.follow-icons span{width:30px;height:28px;background:#3d6aa6;border-radius:2px}

.legal{top:903px;font-size:12px;color:var(--olive)}
.login{left:968px;top:894px;width:59px;height:32px;border-radius:8px;background:linear-gradient(#f57b2e,var(--login));color:#fff;font-size:13px;display:flex;align-items:center;justify-content:center}

.side-tabs{left:1090px;top:238px;width:112px;height:292px;background:linear-gradient(90deg,#f4f4f4,#fff);border-radius:12px 0 0 12px;box-shadow:-2px 2px 6px rgba(0,0,0,.2)}
.side-item{position:absolute;left:0;width:112px;text-align:center;font-size:12px;color:#444;letter-spacing:.5px}
.side-icon{position:absolute;left:34px;width:44px;height:46px;border-radius:4px}
.side-item.active{background:#e2e2e2}

.modal-frame{left:362px;top:162px;width:678px;height:541px;background:var(--modal-frame);border-radius:22px}
.modal{left:383px;top:183px;width:635px;height:500px;background:var(--modal-bg)}
.modal-icon{left:433px;top:195px;width:55px;height:52px;background:linear-gradient(#dfe8ee,#8fb7d0);border-radius:3px}
.modal-title{left:505px;top:208px;font-family:"Open Sans",sans-serif;font-size:28px;color:#111}
.form-box{left:427px;top:263px;width:547px;height:394px;background:#f2f2f2;border:1px solid #d8d8d8;border-radius:6px}
.form-label{left:428px;width:119px;background:var(--label);font-family:"Open Sans",sans-serif;font-size:14px;color:#333;display:flex;align-items:flex-start;padding:14px 0 0 14px;gap:10px;border-radius:4px 0 0 4px}
.form-label svg{flex:none}
.form-field{left:547px;width:410px;background:var(--field);border-radius:0 4px 4px 0;font-family:"Noto Serif",serif;font-style:italic;font-size:14px;color:#9a9a9a;padding:13px 0 0 14px}
.form-btn{top:602px;height:36px;font-family:"Open Sans",sans-serif;font-size:14px;font-weight:700;color:#333;border-radius:4px}
</style>
</head>
<body>

<div class="abs cookie-tab">Cookie policy agreement</div>

<div class="abs brand"><span class="brand-mark"></span><span class="brand-name">TOVEN</span></div>

<nav class="abs main-nav"><span>HOME</span><span>ABOUT</span><span>PORTFOLIO</span><span>JOBS</span><span>CONTACT</span></nav>

<div class="abs page"></div>

<div class="abs hero"></div>
<div class="abs hero-art" role="img" aria-label="Montage of technology imagery: eye scan and glass skyscraper"></div>
<div class="abs hero-title">Our passion is developing complex applications for the web</div>

<div class="abs section-title" style="left:161px;top:377px">Our Services</div>
<div class="abs service-card"></div>
<div class="abs service-icon" role="img" aria-label="Screwdriver and wrench illustration"></div>
<p class="abs service-text">We can turn your business processes into online web applications.We can turn your</p>
<div class="abs service-card-2">W<br>o</div>
<div class="abs btn-grey" style="left:242px;top:585px;width:96px;height:23px;font-weight:600">Read More</div>

<div class="abs num-accent" style="left:1038px;top:419px">12</div>
<div class="abs link-accent" style="left:1038px;top:456px">rn</div>
<div class="abs num-accent" style="left:1038px;top:495px">12</div>
<div class="abs link-accent" style="left:1038px;top:532px">rn</div>

<div class="abs clients-bar">Clients</div>
<div class="abs client-box"></div>
<div class="abs client-name">Lumaris</div>
<div class="abs btn-grey" style="left:106px;top:798px;width:116px;height:32px;font-weight:600">Full Clients List</div>
<div class="abs circle-btn" style="left:333px;top:803px"></div>
<div class="abs circle-btn" style="left:359px;top:803px"></div>

<div class="abs news-date" style="left:650px;top:716px">467 days ago</div>
<p class="abs news-text" style="left:436px;top:748px;width:290px">Lorem ipsum dolor sit amet, consec tetuer adipiscing elit. Praesent ves tibulum molestie lacus.</p>
<div class="abs news-date" style="left:650px;top:790px">467 days ago</div>
<div class="abs btn-grey" style="left:434px;top:797px;width:60px;height:30px;color:#888">More</div>

<p class="abs testimonial">adipiscing elit. Praesent ves tibulum molestie lacus.Praesent ves tibulum molestie lacus.Praesent ves tibulum molestie lacus.Praesent ves tibulum molestie lacus.Praesent ves tibulum molestie lacus.</p>
<div class="abs testimonial-author">Sdhftgut , AUS</div>
<div class="abs avatar" role="img" aria-label="Client silhouette placeholder"></div>

<div class="abs footer-band"></div>
<div class="abs share-strip">
  <span class="share-btn">tweet</span>
  <span class="share-btn">Submit</span>
  <span class="share-btn">Like</span><span class="share-count">0</span>
  <span class="share-btn" style="margin-left:20px">+1</span><span class="share-count">0</span>
</div>
<div class="abs follow-label">Follow Us</div>
<div class="abs follow-icons" aria-label="Social network links"><span></span><span style="background:#3fa6d8"></span><span style="background:#1f6aa0"></span><span style="background:#2f6d93"></span></div>

<div class="abs legal" style="left:128px">© Toven Ltd. 2012 Registered in England &amp; Wales Number: 06183427.</div>
<div class="abs legal" style="left:590px">Terms and Conditions | Privacy Policy | Cookie Policy | Site Map</div>
<div class="abs login">login</div>

<div class="abs side-tabs">
  <div class="side-icon" style="top:18px;background:linear-gradient(#bfe0f5,#4a8fc8)" role="img" aria-label="Portfolio picture frames icon"></div>
  <div class="side-item" style="top:75px">PORTFOLIO</div>
  <div class="side-item active" style="top:100px;height:86px"></div>
  <div class="side-icon" style="top:108px;background:linear-gradient(#f2f2f2,#bbb)" role="img" aria-label="Figure pushing a block icon"></div>
  <div class="side-item" style="top:163px;text-align:left;padding-left:5px">GET IN TOUCH H</div>
  <div class="side-icon" style="top:202px;background:linear-gradient(#777,#444)" role="img" aria-label="Shared folder icon"></div>
  <div class="side-item" style="top:256px">SHARE</div>
</div>
<div class="abs circle-btn" style="left:1082px;top:311px"></div>
<div class="abs circle-btn" style="left:1082px;top:490px"></div>
<svg class="abs" style="left:1033px;top:377px" width="56" height="42" viewBox="0 0 56 42" aria-hidden="true">
  <path d="M0 11h30V0l26 21-26 21V31H0z" fill="#3c9fd0"/>
</svg>

<div class="abs modal-frame"></div>
<div class="abs modal"></div>
<div class="abs modal-icon" role="img" aria-label="Envelope and pen icon"></div>
<h1 class="abs modal-title" style="font-weight:400">Contact Us</h1>
<div class="abs form-box"></div>

<div class="abs form-label" style="top:281px;height:42px"><svg width="14" height="14" viewBox="0 0 14 14"><circle cx="7" cy="4" r="3" fill="#4a7ea8"/><path d="M1 14c0-4 3-6 6-6s6 2 6 6z" fill="#4a7ea8"/></svg>Name</div>
<div class="abs form-field" style="top:281px;height:42px">Type your name here...</div>

<div class="abs form-label" style="top:337px;height:42px"><svg width="16" height="12" viewBox="0 0 16 12"><rect x=".5" y=".5" width="15" height="11" fill="#fff" stroke="#8aa"/><path d="M1 1l7 6 7-6" fill="none" stroke="#8aa"/></svg>Email</div>
<div class="abs form-field" style="top:337px;height:42px">Type your email address here...</div>

<div class="abs form-label" style="top:393px;height:42px"><svg width="12" height="15" viewBox="0 0 12 15"><rect x=".5" y=".5" width="11" height="14" fill="#fff" stroke="#8aa"/><path d="M3 5h6M3 8h6M3 11h6" stroke="#8aa"/></svg>Subject</div>
<div class="abs form-field" style="top:393px;height:42px">Type your subject here...</div>

<div class="abs form-label" style="top:449px;height:42px"><svg width="15" height="15" viewBox="0 0 15 15"><path d="M2 13l1-4 8-8 3 3-8 8z" fill="#e0b640" stroke="#8a6a20"/></svg>Message</div>
<div class="abs form-field" style="top:449px;height:136px;border-radius:0 4px 4px 4px">Type your message here...</div>

<div class="abs btn-grey form-btn" style="left:547px;width:96px">SUBMIT</div>
<div class="abs btn-grey form-btn" style="left:656px;width:87px">RESET</div>

</body>
</html>
```